Business Card Design Project

We require a business card design to go with our new logo for our Valorix business.
The card must have some information on it prescribed by our licensee, as well as our contact details.
There are 3 cards we need for each of our Advisers, I'm happy to amend/edit the design with each of our details, or for you to do all 3 for us. Most of the details on each will remain the same, but our names, qualifications and mobile numbers will differ on each.
I have attached the mock-up from our licensee. As you can see it is very plain looking. As long as the licensee logo (Harwick Stanton) and the sentence "Authorised Representative of Harwick Stanton Limited - Australian Financial Services Licensee" appears on it we will be compliant.
Our new Valorix logo black on white and white on black has been uploaded for your design. This is our main logo, the Harwick Stanton logo is a small/minor secondary one.
I have uploaded a separate Harwick Stanton Logo as well.
Of the logos you created for us, we like the idea of having the white with black text on the front, and the black with white text filling the back of the card - but do what ever you feel will look the best.
It is up to you what the fonts, colours, locations etc of the content of the cards etc. will be.
Content
These are the details that will be different on each card:
Name: Gordon Whitlaker
Job Title: Director | Financial Adviser
Qualifications: B Bus Mgmt, B Bus IS, DFP (Fin Serv)
Mob: 0482 946 517
E: gordon@valorix.com.au
Name: Simon Treloar
Qualifications: DFP (Fin Serv), Adv Dip (Acc)
Mob: 0461 293 784
E: simon@valorix.com.au
Name: Neil Bramwell
Qualifications: DFP (Fin Serv)
Mob: 0473 615 938
E: neil@valorix.com.au
These are the details that will be the same on each card:
T: 08 9571 3842
F: 08 9571 6429
M: (as above)
E: xxxx@valorix.com.au
Unit 7, 18 Corbett Street
MARLOW HEIGHTS WA 6093
PO Box 86
DRAYFORD WA 6947
Plus the Harwick Stanton logo and text.
If you want to design with 1 persons details until the design is finalised just use mine and we can amend the others last thing.
Updates
Hi, Thanks for your submissions so far, but I must apologise, I thought this project was restricted so I didn't upload our business logo for Valorix. I have since uploaded our business logo for your use. The Harwick Stanton logo needs to be on the card as per the mock-up word doc, but it only needs to be a small/secondary logo as this is the logo of our licensee (not our business), so the main one is our new Valorix logo. Thank you.
Industry/Entity Type
Business
Requirements
Must have
- Harwick Stanton logo and text
Adviser contact details

```html
<!DOCTYPE html>
<html lang="en">
<head>
<meta charset="utf-8">
<title>Valorix Business Card</title>
<link href="https://fonts.googleapis.com/css2?family=Source+Sans+3:wght@400;600;700&display=swap" rel="stylesheet">
<style>
  :root {
    --backdrop: #2a2a2a;
    --card-white: #ffffff;
    --card-black: #0b0b0b;
    --ink: #1f1f1f;
    --ink-soft: #3a3a3a;
    --accent: #ee6a1f;
    --silver: #e6e6e6;
    --grey-mark: #8a8a8a;
  }
  * { box-sizing: border-box; margin: 0; padding: 0; }
  html, body {
    width: 1200px; height: 900px; overflow: hidden;
    background: var(--backdrop);
    font-family: "Source Sans 3", Arial, sans-serif;
  }
  .stage {
    width: 1200px; height: 900px;
    display: flex; align-items: center; justify-content: center; gap: 40px;
  }
  .card {
    position: relative;
    width: 540px; height: 310px;
    box-shadow: 0 10px 30px rgba(0,0,0,.45);
    overflow: hidden;
  }

  /* Front */
  .card--front { background: var(--card-white); color: var(--ink); }
  .card--front .accent-band {
    position: absolute; left: 0; right: 0; bottom: 0; height: 12px;
    background: var(--accent);
  }
  .brand {
    position: absolute; top: 26px; right: 30px;
    display: flex; align-items: center; gap: 10px;
  }
  .brand__dot { width: 34px; height: 34px; border-radius: 50%; background: var(--ink); }
  .brand__name { font-size: 24px; font-weight: 700; letter-spacing: 3px; color: var(--ink); text-transform: uppercase; }

  .details { position: absolute; left: 34px; top: 26px; width: 300px; font-size: 12.5px; line-height: 1.35; color: var(--ink-soft); }
  .adviser__name { color: var(--accent); font-weight: 700; font-size: 20px; letter-spacing: .5px; text-transform: uppercase; line-height: 1.1; }
  .adviser__role { font-size: 12.5px; }
  .adviser__quals { font-size: 11.5px; }
  .rule { height: 1px; background: var(--accent); margin: 7px 0; width: 210px; }
  .label { color: var(--accent); }
  .contact strong { color: var(--ink); font-weight: 700; }

  .licensee {
    position: absolute; right: 30px; bottom: 30px; width: 250px; text-align: right;
    font-size: 10.5px; line-height: 1.3; color: var(--ink-soft);
  }
  .licensee__mark { display: flex; justify-content: flex-end; align-items: center; gap: 6px; margin-bottom: 4px; }
  .licensee__dot { width: 14px; height: 14px; border-radius: 50%; background: var(--grey-mark); }
  .licensee__name { font-weight: 700; font-size: 11.5px; letter-spacing: .5px; color: var(--ink); text-transform: uppercase; }

  /* Back */
  .card--back {
    background: var(--card-black);
    display: flex; flex-direction: column; align-items: center; justify-content: center; gap: 26px;
  }
  .back-brand { display: flex; align-items: center; gap: 18px; }
  .back-brand__dot { width: 40px; height: 40px; border-radius: 50%; background: var(--silver); }
  .back-brand__name { font-size: 54px; font-weight: 400; letter-spacing: 12px; color: var(--silver); text-transform: uppercase; }
  .website { font-size: 16px; color: var(--silver); letter-spacing: .5px; }
  .website span { color: var(--accent); font-weight: 700; }
</style>
</head>
<body>
<main class="stage">
  <section class="card card--front">
    <div class="brand">
      <span class="brand__dot"></span>
      <span class="brand__name">Valorix</span>
    </div>

    <div class="details">
      <p class="adviser__name">Gordon Whitlaker</p>
      <p class="adviser__role">Director | Financial Adviser</p>
      <p class="adviser__quals">B Bus Mgmt, B Bus IS, DFP (Fin Serv)</p>
      <div class="rule"></div>
      <p class="contact"><span class="label">Mob:</span> 0482 946 517</p>
      <p class="contact"><span class="label">Email:</span> <strong>gordon</strong>@valorix.com.au</p>
      <div class="rule"></div>
      <p>Unit 7, 18 Corbett Street</p>
      <p>MARLOW HEIGHTS WA 6093</p>
      <p>PO Box 86</p>
      <p>DRAYFORD WA 6947</p>
      <div class="rule"></div>
      <p class="contact"><span class="label">Tel:</span> 08 9571 3842 <span class="label">Fax:</span> 08 9571 6429</p>
      <p class="contact">Email: xxxx@valorix.com.au</p>
    </div>

    <div class="licensee">
      <div class="licensee__mark">
        <span class="licensee__dot"></span>
        <span class="licensee__name">Harwick Stanton</span>
      </div>
      <p>Authorised Representative of Harwick Stanton Limited - Australian Financial Services Licensee</p>
    </div>

    <div class="accent-band"></div>
  </section>

  <section class="card card--back">
    <div class="back-brand">
      <span class="back-brand__dot"></span>
      <span class="back-brand__name">Valorix</span>
    </div>
    <p class="website">www.<span>valorix.com</span>.au</p>
  </section>
</main>
</body>
</html>
```